Business Card Design

I need a business card design for my new business based on Long Island, NY also serving NYC called Pine Hollow Kennel. I have built a website with printwell that can be looked at as a basis for the card. It is pinehollowkennel.example.

I board Labrador Retrievers in my home. Specialize in one breed. Cage free environment. Dogs have full run of home and fenced in property. Pine Hollow Kennel is a one-of-a-kind, high-quality dog-boarding provider serving specifically Labrador Retrievers. By working with a dog I am comfortable with, I am able to offer the best care for all pets that come through my door. I work with Lab owners in the Long Island/NYC area to provide an
in-home safe, reliable and fun environment for daycare and overnight stays.

I provide a unique boarding experience for Labrador Retrievers on Long Island. Your Lab should be well mannered, housebroken and good with other dogs. Provided your pet is well mannered and house trained, my boarding services allow dogs to experience a cage-free stay while having free roam of my home and property. This allows owners a unique alternative to a kennel, giving pets the chance to experience a home away from home rather than chain linked fences and cold concrete floors.
As a guest at Pine Hollow Kennel, your dog will get:

4-star kibble
Access to my in-ground pool
All-natural snack selection
Companionship of other retrievers including my two
Full run of entire home and fenced-in backyard
Photos AND videos posted to Chatterpage so you can see your dog having fun while away
Toys, bones and affection

I think it is important to have a pic of the 3 colored labs below. Also the picture of my own personal labs ..the white one with the black puppy. Maybe some paw prints. If using any imagery that MUST look EXACTLY like labrador retriever no generic dogs. Thank you
Updates

The Back of the Card should have the following: The background should be one of the pictures I sent (white dog in pool or another pic I included) At Pine Hollow Kennel your Lab gets: Cage Free Environment Full run of my home and fenced in yard In-ground pool Toys and affection Companionship of other Labrador Retrievers Photos and Videos posted Chatterpage of your loved one FRONT OF THE CARD: should include picture of the 3 labs (yellow white brown) OR picture of white dog in pool. Pine Hollow Kennel should be in larger font than the rest. the following can be in any order. Rick Dunmore Commack, NY in Central Long Island pinehollowkennel.example 631-555-0194

Industry/Entity Type

Environment

Contact Information for Business Card

Pine Hollow Kennel
Commack, NY
Rick Dunmore
pinehollowkennel@mailbox.example
631-555-0194

```html
<!DOCTYPE html>
<html lang="en">
<head>
<meta charset="utf-8">
<title>Pine Hollow Kennel – Business Card</title>
<link href="https://fonts.googleapis.com/css2?family=Dosis:wght@500;600;700&family=Arimo:wght@400&display=swap" rel="stylesheet">
<style>
  :root {
    --page: #ece7e1;
    --paper: #ffffff;
    --mint: #72cfb6;
    --sky: #a6dde6;
    --cloud: #eaf5f8;
    --grey-word: #9b9b9b;
    --ink: #1d1d1f;
    --body-ink: #4a4a4a;
    --edge-band: #45454d;
    --grass: #6f8a4a;
    --coat-dark: #3a2a22;
  }
  * { box-sizing: border-box; margin: 0; padding: 0; }
  html, body {
    width: 1200px; height: 848px; overflow: hidden;
    background: var(--page);
  }
  .canvas { position: relative; width: 1200px; height: 848px; }
  .card {
    position: absolute; left: 280px; width: 640px; height: 366px;
    background: var(--paper);
    box-shadow: 0 6px 18px rgba(0,0,0,.18);
    overflow: hidden;
  }
  .card--front { top: 40px; }
  .card--back { top: 442px; }

  /* Front */
  .front-art { position: absolute; left: 0; top: 0; width: 640px; height: 270px; display: block; }
  .brand-block {
    position: absolute; left: 440px; top: 60px; width: 180px;
    font-family: "Dosis", sans-serif; font-weight: 700;
    font-size: 34px; line-height: 1.12; text-align: center;
    letter-spacing: .5px; text-transform: uppercase;
  }
  .brand-block .brand-name { color: var(--mint); display: block; }
  .brand-block .brand-town { color: var(--grey-word); display: block; font-size: 30px; }
  .front-footer {
    position: absolute; left: 0; top: 270px; width: 640px; height: 96px;
    display: flex; align-items: center; justify-content: space-between;
    padding: 0 30px 0 34px;
  }
  .owner-name {
    font-family: "Dosis", sans-serif; font-weight: 700; font-size: 38px;
    color: var(--mint); text-transform: uppercase; letter-spacing: .5px;
  }
  .contact-list { list-style: none; font-family: "Dosis", sans-serif; font-weight: 600; font-size: 14px; color: var(--ink); }
  .contact-list li { display: flex; align-items: center; gap: 10px; line-height: 1.7; }
  .contact-list svg { width: 16px; height: 14px; flex: none; }

  /* Back */
  .guest-banner {
    position: absolute; left: 0; top: 0; width: 604px; height: 86px;
    background: var(--sky);
    padding: 14px 22px;
  }
  .guest-banner h2 {
    height: 100%; border: 4px solid var(--mint);
    background: var(--paper);
    display: flex; align-items: center; justify-content: center;
    font-family: "Dosis", sans-serif; font-weight: 700; font-size: 21px;
    color: var(--mint); text-transform: uppercase; letter-spacing: .6px;
  }
  .edge-band { position: absolute; right: 0; top: 0; width: 36px; height: 100%; background: var(--edge-band); }
  .perk-list {
    position: absolute; left: 0; top: 112px; width: 604px;
    list-style: none; text-align: center;
    font-family: "Arimo", sans-serif; font-size: 15.5px; line-height: 1.42; color: var(--body-ink);
  }
</style>
</head>
<body>
<main class="canvas">

  <section class="card card--front" aria-label="Card front">
    <svg class="front-art" viewBox="0 0 640 270" xmlns="http://www.w3.org/2000/svg">
      <defs>
        <linearGradient id="photoTone" x1="0" y1="0" x2="1" y2="1">
          <stop offset="0" stop-color="#7d9a55"/>
          <stop offset=".45" stop-color="#c9bfa4"/>
          <stop offset="1" stop-color="#2e2622"/>
        </linearGradient>
      </defs>
      <rect class="panel-sky" width="640" height="270" fill="#a6dde6"/>
      <path class="panel-cloud" d="M410 62 A55 55 0 0 1 500 20 A46 46 0 0 1 585 34 L640 34 V270 H472 A60 60 0 0 1 404 200 A56 56 0 0 1 410 62 Z" fill="#eaf5f8"/>
      <path class="dog-photo" role="img" aria-label="Photo of three Labrador Retrievers, chocolate, yellow and black, sitting on grass"
            d="M0 0 H292 A60 60 0 0 1 346 72 A56 56 0 0 1 338 192 A62 62 0 0 1 276 250 H22 A22 22 0 0 1 0 228 Z" fill="url(#photoTone)"/>
    </svg>

    <h1 class="brand-block">
      <span class="brand-name">Pine Hollow Kennel</span>
      <span class="brand-town">Commack</span>
    </h1>

    <div class="front-footer">
      <p class="owner-name">NY Rick Dunmore</p>
      <ul class="contact-list">
        <li>
          <svg viewBox="0 0 16 14" aria-hidden="true"><rect x="1" y="2" width="14" height="10" fill="none" stroke="#1d1d1f" stroke-width="1.6"/><path d="M1 2 L8 8 L15 2" fill="none" stroke="#1d1d1f" stroke-width="1.6"/></svg>
          pinehollowkennel@mailbox.example
        </li>
        <li>
          <svg viewBox="0 0 16 14" aria-hidden="true"><path d="M3 1 L6 1 L7 4 L5 5.5 C6 8 7.5 9.5 10 10.5 L11.5 8.5 L14.5 9.5 L14.5 12.5 C9 13.5 2 7 3 1 Z" fill="#1d1d1f"/></svg>
          631-555-0194
        </li>
      </ul>
    </div>
  </section>

  <section class="card card--back" aria-label="Card back">
    <div class="guest-banner">
      <h2>As a guest at Pine Hollow Kennel, your dog will get</h2>
    </div>
    <ul class="perk-list">
      <li>4-star kibble</li>
      <li>Access to my in-ground pool</li>
      <li>All-natural snack selection</li>
      <li>Companionship of other retrievers including my two</li>
      <li>Full run of entire home and fenced-in backyard</li>
      <li>Photos AND videos posted to Chatterpage<br>so you can see your dog having fun while away</li>
      <li>Toys, bones and affection</li>
    </ul>
    <div class="edge-band"></div>
  </section>

</main>
</body>
</html>
```